Events Online Video Streaming Company

A website needs to be designed to replace the current website of a company that specialises in providing an online portal for streaming events to users. the current portal exists at: http://www.qulmora.com <- designers can get a "feel" for what they do and the content they require from this existing website.
the current qulmora logo and green color are to be maintined. i will upload an EPS of the logo soon.
The new design needs to highlight the main aspects of what they do: live streaming of events, multiple cameras, online chat, user activity data (like zintro dashtrack), customised front-ends.
we want the design to be in-between a corporate feel and modern, contemporary. ie. we dont want it to be too corporate (like the current website).
the design must also incorporate the word: glimmerfolk as part of their slogan or sub-title.
hi everyone,

```html
<!DOCTYPE html>
<html lang="en">
<head>
<meta charset="utf-8">
<title>Qulmora – Live Social Media Integrated Portal</title>
<link href="https://fonts.googleapis.com/css2?family=Open+Sans:ital,wght@0,400;0,600;0,700;1,400&display=swap" rel="stylesheet">
<style>
:root{
  --green:#8cc63f;
  --green-light:#a6d96a;
  --green-pale:#e6f5cf;
  --dark:#1c1c1c;
  --charcoal:#3a3a3a;
  --grey-tile:#6d6d6d;
  --grey-band:#e4e4e4;
  --grey-soft:#f6f6f6;
  --grey-panel:#ececec;
  --text:#444;
  --white:#fff;
  --c-sport:#0c9a48;
  --c-edu:#1a9bd7;
  --c-comm:#8a22b3;
  --c-gigs:#c4177f;
  --c-conf:#f0c02b;
  --c-else:#3d3d3d;
}
*{box-sizing:border-box;margin:0;padding:0}
html,body{width:678px;height:1200px;overflow:hidden}
body{font-family:"Open Sans",Arial,sans-serif;color:var(--text);background:var(--white);position:relative}
.abs{position:absolute}

/* header */
.header{left:0;top:0;width:678px;height:59px;background:var(--white)}
.brand{left:61px;top:14px;font-size:31px;font-weight:600;color:var(--green);letter-spacing:-1px;line-height:1}
.brand-dot{display:inline-block;width:9px;height:9px;border-radius:50%;background:var(--green);margin-left:4px;vertical-align:top}
.divider{left:204px;top:12px;width:1px;height:40px;background:#e2e2e2}
.tagline{left:221px;top:28px;font-size:10px;color:var(--green);letter-spacing:.3px}
.hero-photo{left:356px;top:0;width:322px;height:208px;background:linear-gradient(160deg,#9cc46a 0%,#6f9a3e 40%,#c9d4c8 70%,#8fb060 100%);clip-path:polygon(0 0,100% 0,100% 100%,26% 100%,16% 78%,12% 55%,0 55%)}
.nav{left:0;top:59px;width:455px;height:37px;background:linear-gradient(#3b3b3b,#111);border-radius:0 0 6px 0;display:flex;gap:18px;padding-left:70px;align-items:center}
.nav a{color:var(--white);text-decoration:none;font-size:9.5px;font-weight:600;letter-spacing:.2px}
.hero{left:0;top:96px;width:678px;height:112px;background:linear-gradient(#eaeaea,#dcdcdc);z-index:-1}
.hero-title{left:57px;top:112px;font-size:17px;font-weight:700;color:#444;line-height:21px;letter-spacing:.2px}
.hero-title span{color:var(--green)}
.hero-icons{left:57px;top:168px;display:flex;gap:1px}
.hero-icons div{width:30px;height:30px;background:var(--green);display:flex;align-items:center;justify-content:center}
.btn-contact{left:343px;top:175px;width:69px;height:20px;background:linear-gradient(#3a3a3a,#111);color:var(--white);font-size:8.5px;border-radius:3px;display:flex;align-items:center;justify-content:center}

/* features */
.features{left:0;top:208px;width:678px;height:173px;background:var(--grey-soft)}
.tile-grid{left:57px;top:227px;display:grid;grid-template-columns:repeat(4,61px);gap:2px}
.tile{height:63px;background:var(--grey-tile);border:1px solid #555;color:#f0f0f0;font-size:7.5px;text-align:center;display:flex;flex-direction:column;justify-content:center;line-height:10px;padding:0 2px}
.tile b{font-weight:400;margin-top:6px}
.tile.active{background:var(--green-light);border-color:var(--green);color:#2f4d10}
.feature-num{left:370px;top:258px;width:20px;height:20px;background:var(--green-light);font-size:10px;color:#333;display:flex;align-items:center;justify-content:center}
.feature-title{left:399px;top:260px;font-size:12px;color:#333}
.feature-text{left:370px;top:288px;width:205px;font-size:7px;line-height:12px;color:#555}

/* categories */
.category-band{left:0;top:381px;width:678px;height:183px;background:linear-gradient(#a9d86b,var(--green))}
.cards{left:58px;top:418px;display:flex;gap:3.5px}
.card{width:91.5px;height:113px;background:var(--white);border:1px solid #ddd;position:relative}
.card h3{height:28px;color:var(--white);font-size:9px;font-weight:400;text-align:center;padding-top:14px}
.card p{font-size:6.3px;line-height:9px;color:#555;padding:4px 4px 0}
.card .more{position:absolute;left:3px;right:3px;bottom:4px;height:20px;color:var(--white);font-size:7.5px;border-radius:2px;display:flex;align-items:center;justify-content:center;gap:10px}

/* showcase */
.showcase{left:0;top:564px;width:420px;height:421px;background:var(--grey-soft)}
.side{left:420px;top:564px;width:258px;height:421px;background:var(--grey-panel)}
.item{position:absolute;width:113px;text-align:center}
.item.active{background:var(--green-pale)}
.item .pic{width:103px;height:76px;margin:5px auto 0}
.item h4{font-size:9.5px;font-weight:400;color:#222;margin-top:12px;line-height:11px}
.item p{font-size:6.3px;font-style:italic;line-height:10px;color:#555;margin-top:8px;padding:0 3px}
.rule{position:absolute;width:108px;height:1px;background:#999}
.pic-globe{background:radial-gradient(circle at 55% 60%,#3a78c9,#0d2450 60%,#04102a)}
.pic-people{background:linear-gradient(135deg,#e9ecef,#bfc6cf 50%,#3d4050)}
.pic-desk{background:linear-gradient(135deg,#f1f1f1,#c9c9c9 55%,#6a7078)}
.side-pic{left:432px;top:586px;width:182px;height:134px;border:3px solid var(--white)}
.side-title{left:434px;top:731px;font-size:16.5px;color:#333}
.side-text{left:434px;top:762px;width:185px;font-size:7px;line-height:11.3px;color:#555}
.side-text p{margin-bottom:11px}
.side-text a{color:var(--green);text-decoration:none}

/* footer */
.footer{left:0;top:985px;width:678px;height:189px;background:var(--dark)}
.fcol{position:absolute;top:1007px;color:var(--white);font-size:6.8px;line-height:11.3px;font-weight:600}
.fcol h5{color:var(--green);font-size:8px;font-weight:700;margin-bottom:10px}
.signup{width:123px;height:20px;background:var(--white);margin-top:8px;display:flex;justify-content:space-between;align-items:center;padding-left:6px;color:#555;font-style:italic;font-weight:400}
.signup span{width:16px;height:16px;margin-right:2px;background:var(--green)}
.social{display:flex;gap:3px;margin-top:4px}
.social div{width:16px;height:16px;background:var(--green)}
.copy-bar{left:0;top:1174px;width:678px;height:26px;background:var(--green);font-size:6.8px;color:#222;font-weight:600;padding:9px 0 0 65px}
</style>
</head>
<body>

<div class="abs header"></div>
<div class="abs brand">qulmora<span class="brand-dot"></span></div>
<div class="abs divider"></div>
<div class="abs tagline">GLIMMERFOLK</div>
<div class="abs hero"></div>
<div class="abs hero-photo" role="img" aria-label="Photo of a young woman lying on a lawn using a laptop"></div>
<nav class="abs nav"><a>HOME</a><a>FEATURES</a><a>APPLICATIONS</a><a>THE TEAM</a><a>SUPPORT</a><a>CONTACT US</a></nav>
<h1 class="abs hero-title">WELCOME TO <span>QUL</span>MORA A LIVE<br>SOCIAL MEDIA INTEGRATED PORTAL</h1>
<div class="abs hero-icons">
  <div></div>
  <div><svg width="18" height="18" viewBox="0 0 18 18"><circle cx="9" cy="9" r="8" fill="none" stroke="#fff" stroke-width="2"/><path d="M7 5.5v7l5.5-3.5z" fill="#fff"/></svg></div>
  <div></div>
  <div></div>
  <div><svg width="18" height="18" viewBox="0 0 18 18"><ellipse cx="9" cy="8" rx="7" ry="5.5" fill="none" stroke="#fff" stroke-width="2"/><path d="M10 13l3 3v-4" fill="#fff"/></svg></div>
</div>
<div class="abs btn-contact">Contact us</div>

<section class="abs features"></section>
<div class="abs tile-grid">
  <div class="tile active">INNOVATION/<br>TECHNOLOGY<b>1</b></div>
  <div class="tile">SOCIAL MEDIA,<br>NETWORKING<b>2</b></div>
  <div class="tile">LIVE VIDEO<br>STREAMING<b>3</b></div>
  <div class="tile">VIDEO ON<br>DEMAND<b>4</b></div>
  <div class="tile">ANALYTICAL<br>REPORTING<b>5</b></div>
  <div class="tile">SPONSOR/<br>ADVERTISING<b>6</b></div>
  <div class="tile">ANY DEVICE,<br>NO INSTALL<b>7</b></div>
  <div class="tile">EASY TO USE<b>8</b></div>
</div>
<div class="abs feature-num">1</div>
<h2 class="abs feature-title">INNOVATION / TECHNOLOGY</h2>
<p class="abs feature-text">Developments such as mobile devices, mobile internet, video streaming, cloud computing, and web development systems have made it possible for us to develop Qulmora with the use of the lastest innovative technologies.</p>

<section class="abs category-band"></section>
<div class="abs cards">
  <div class="card"><h3 style="background:var(--c-sport)">sport</h3><p>View live sports events, check out the stats, and chat with friends about the game.</p><div class="more" style="background:var(--c-sport)">MORE INFO <span>›</span></div></div>
  <div class="card"><h3 style="background:var(--c-edu)">education</h3><p>With much of todays learning being based off campus, Qulmora is an effective educational tool.</p><div class="more" style="background:var(--c-edu)">MORE INFO <span>›</span></div></div>
  <div class="card"><h3 style="background:var(--c-comm)">communication</h3><p>Qulmora is a great communication tool for business with broadcast, discussion and feedback systems built in.</p><div class="more" style="background:var(--c-comm)">MORE INFO <span>›</span></div></div>
  <div class="card"><h3 style="background:var(--c-gigs)">gigs &amp; festivals</h3><p>What to see a band but its sold out, watch it live online, while chatting with your friends.</p><div class="more" style="background:var(--c-gigs)">MORE INFO <span>›</span></div></div>
  <div class="card"><h3 style="background:var(--c-conf)">conferences</h3><p>Too busy to attend the event, attend virtually instead and don't miss out on content or social.</p><div class="more" style="background:var(--c-conf)">MORE INFO <span>›</span></div></div>
  <div class="card"><h3 style="background:var(--c-else)">what else?</h3><p>Qulmora has a multitude of uses with many ideas in development. Have an idea? Drop us a line.</p><div class="more" style="background:var(--c-else)">MORE INFO <span>›</span></div></div>
</div>

<section class="abs showcase"></section>
<aside class="abs side"></aside>

<div class="item active" style="left:57px;top:584px;height:183px">
  <div class="pic pic-globe" role="img" aria-label="Illustration of a glowing globe with network lines"></div>
  <h4>Secure event content</h4>
  <p>Qulmora allows event organisers to diversify their event income streams by adding revenue from virtual delegates as well as industry partners or sponsors of the event portal.</p>
</div>
<div class="item" style="left:177px;top:584px">
  <div class="pic pic-people" role="img" aria-label="Photo of smiling conference delegates"></div>
  <h4>Latest technology</h4>
  <p>Qulmora combines the very latest technologies into a portal that now makes it possible to attend an event online, while still getting many of the benefits of onsite attendance.</p>
</div>
<div class="item" style="left:298px;top:584px">
  <div class="pic pic-desk" role="img" aria-label="Photo of a man working on a laptop"></div>
  <h4>Attend from anywhere in the world</h4>
  <p>You can access Qulmora on any internet-connected device so you can watch, listen, contribute, discuss and connect with the event.</p>
</div>
<div class="rule" style="left:60px;top:767px"></div>
<div class="rule" style="left:180px;top:767px"></div>
<div class="rule" style="left:300px;top:767px"></div>

<div class="item" style="left:57px;top:773px">
  <div class="pic pic-globe" role="img" aria-label="Illustration of a glowing globe with network lines"></div>
  <h4>Secure event content</h4>
  <p>Qulmora allows event organisers to diversify their event income streams by adding revenue from virtual delegates as well as industry partners or sponsors of the event portal.</p>
</div>
<div class="item" style="left:177px;top:773px">
  <div class="pic pic-people" role="img" aria-label="Photo of smiling conference delegates"></div>
  <h4>Latest technology</h4>
  <p>Qulmora combines the very latest technologies into a portal that now makes it possible to attend an event online, while still getting many of the benefits of onsite attendance.</p>
</div>
<div class="item" style="left:298px;top:773px">
  <div class="pic pic-desk" role="img" aria-label="Photo of a man working on a laptop"></div>
  <h4>Attend from anywhere in the world</h4>
  <p>You can access Qulmora on any internet-connected device so you can watch, listen, contribute, discuss and connect with the event.</p>
</div>
<div class="rule" style="left:60px;top:958px"></div>
<div class="rule" style="left:180px;top:958px"></div>
<div class="rule" style="left:300px;top:958px"></div>

<div class="abs side-pic pic-globe" role="img" aria-label="Illustration of a glowing globe with network lines"></div>
<h3 class="abs side-title">Secure event content</h3>
<div class="abs side-text">
  <p>Qulmora allows event organisers to diversify their event income streams by adding revenue from virtual delegates as well as industry partners or sponsors of the event portal. This benefits the event as a whole and everyone involved.</p>
  <p style="margin-bottom:0">Virtual delegates represent an important new income stream for events. Some virtual delegates may have been in a position to attend the event, but for many, virtual attendance was their only option. For most events options for virtual delegates will result in greater delegate numbers and increased income for the event.</p>
  <a>Read more</a>
</div>

<footer class="abs footer"></footer>
<div class="fcol" style="left:62px;width:120px"><h5>Interesting links</h5>Besides are some interesting links for you! Enjoy your stay :)</div>
<div class="fcol" style="left:205px"><h5>Pages</h5>Communications<br>Conferences and conventions<br>Education and training<br>Festivals and Gigs<br>Live video streaming<br>Sporting Events<br>Welcome!<br>Features<br>Applications<br>The Team<br>Support<br>Contact Us</div>
<div class="fcol" style="left:346px;width:125px"><h5>Email Sign up</h5>Keep up-to-date with all of our latest products and special offers<div style="margin-top:6px;font-size:7.5px">Sign up to our newsletter</div><div class="signup">Email address<span></span></div></div>
<div class="fcol" style="left:485px;width:120px"><h5>Contact details</h5>Lorem ipsum dolor sit amet, consectetur adipiscing elit. Proin aliquet, enim quis sagittis rutrum, purus metus posuere nibh, sit<div style="margin-top:11px">info@qulmora.com</div><div style="margin-top:8px;font-size:10px">Stay in touch</div><div class="social"><div></div><div></div><div></div></div></div>
<div class="abs copy-bar">© Copyright 2013- Qulmora</div>

</body>
</html>
```